Modern Can & Tray Design Competition

Please note our brand is now called zé, please do not submit any entries with the wording or logo of "zé kelpwater". Read the full design brief below before making an entry, please.

A competition to design can packaging and outer tray designs for a new exciting brand.

See examples of the design assets I want, below, including both a can and outer tray:

1. https://quillmarketgoods.eu/beverages/energy-drinks/vomba-boost-the-amber-edition-12-x-025-liter-cans-nl/?lang=en

2. https://www.plimvo.com/nl/nl/p/tarvo-fizz-cherry-slim-cans-24-x-330-ml-eu/4812000077312904/

We have 2 flavours in our range, so we need two separate can designs and a separate outer tray design for each flavour.

Our drinks are currently packaged in PET plastic bottles. Our flavours are:
Lemon & Lime - https://zekelpwater.co.uk/products/lemon-and-lime
Strawberry - https://zekelpwater.co.uk/products/strawberry

For this competition, I want can designs for each flavour in 250ml style cans like used by Vomba. And I also want an outer tray for the cans designed for each flavour. Our brand is changing to “zé” so please do not use “kelpwater” on any part of the design. The logo should be “zé” and for each flavour the ze should show the fruit for the flavour embedded inside it. See the files called “ze_fruit_logo_LEMLI (1)” and “ze_fruit_logo_STR (1)” for what I mean. You can use these files for your design.

Under the logo it should state on the can “Prebiotic Fibre Drink”. Similar to how VomBa has “Energy Drink” written under its logo: https://www.drenvilo.com/wp-content/uploads/2009/11/vomba-can-250ml-1.jpg

If you can submit your design ideas for this competition with a picture of the can next to the tray like this for each flavour, that will be best: https://img.keltoshop.com/images/I/57qTzWa2pLx._SL1500_.jpg

So, two design concepts/ideas are needed to enter: One for Lemon & Lime and one for Strawberry.

We want vibrant, eye-catching packaging designs that will catch the consumer's attention.

Right now, we have ze in the centre of our packaging design with fruit embedded in the ze. This must remain a key part of your design as mentioned above. Also, as we will be launching other drinks as a company under different brand names and to unify our different brands we want a splash effect on all the cans which will be replicated across our other brands. So, please have some kind of splash effect on each flavour that can be replicated on the cans of our other brands in future.

Design considerations:

There is also certain information we need on the front/face of the can.

On the very top of the can just below the neck and above the logo we want it to state: “Supports Gut & Overall health*” example: https://pmkgrocerhub.co.uk/wp-content/uploads/2023/10/Brova-Zest-Lemonade.jpg

We also want the number of calories to be stated somewhere on the can in a clever way like in a droplet of the water splash effect. The number of the calories is “17 kcals”.

Under the ze logo as mentioned we want the wording: “Prebiotic Fibre Drink”

Then under Prebiotic Fibre Drink we want the name of the flavour - and then under the flavour we want 3 features stated. Which are:

“20% of daily fibre”
“0g sugar”
“Nothing artificial“

This could be laid out as 3 circles with icons or some other way. The last piece of information under these 3 features is then the size of the can “250 mle”.

In terms of “feel” of the design we want a vibrant colourful feel, and it should show pictures of fruit on it. Here is an example
https://gardenhollowtonics.com/wp-content/uploads/sites/2/2023/03/GHT-US-SodaRange-%E2%80%93-bb-1220x883.png

Any questions let me know. I look forward to seeing your ideas.

To see more about our brand, view our website: www.zekelpwater.co.uk

```html
<!DOCTYPE html>
<html lang="en">
<head>
<meta charset="utf-8">
<title>zé Prebiotic Fibre Drink – Can Designs</title>
<link href="https://fonts.googleapis.com/css2?family=Poppins:wght@300;400;600;700&display=swap" rel="stylesheet">
<style>
  :root {
    --page-bg: #ffffff;
    --alu-light: #f4f4f5;
    --alu-mid: #d9dadc;
    --alu-dark: #c2c3c6;
    --lime: #4cb95a;
    --lime-light: #62d97c;
    --lime-yellow: #f2dc1f;
    --lime-art-a: #e9ef6a;
    --lime-art-b: #8fc74a;
    --lime-art-c: #4e9d3a;
    --berry: #c9252c;
    --berry-art-a: #f0584e;
    --berry-art-b: #d8262d;
    --berry-art-c: #a9141c;
    --white: #ffffff;
  }
  * { box-sizing: border-box; margin: 0; padding: 0; }
  html, body {
    width: 1200px; height: 844px; overflow: hidden;
    background: var(--page-bg);
    font-family: "Poppins", sans-serif;
  }
  .can-face {
    position: absolute; top: 141px;
    width: 218px; height: 578px;
    border-radius: 10px;
    overflow: hidden;
    background: linear-gradient(90deg, var(--alu-dark) 0%, var(--alu-light) 22%, var(--alu-mid) 45%, var(--alu-light) 70%, var(--alu-dark) 100%);
    color: var(--accent);
  }
  .can-face--lemon-lime { left: 264px; --accent: var(--lime); }
  .can-face--strawberry { left: 719px; --accent: var(--berry); }

  .health-band {
    position: absolute; top: 10px; left: 0; right: 0; height: 46px;
    background: var(--accent);
    color: var(--white);
    font-weight: 700; font-size: 10.4px; letter-spacing: 0.1px;
    display: flex; align-items: center; justify-content: center;
    white-space: nowrap;
  }
  .kcal-badge {
    position: absolute; top: 80px; right: 14px;
    width: 39px; height: 39px; border-radius: 3px;
    background: var(--accent); color: var(--white);
    font-weight: 400; line-height: 1; text-align: center;
    display: flex; flex-direction: column; justify-content: center;
  }
  .kcal-badge .kcal-number { font-size: 15px; }
  .kcal-badge .kcal-unit { font-size: 12px; }

  .fruit-art {
    position: absolute; top: 68px; left: 0; right: 0; height: 288px;
  }
  .can-face--lemon-lime .fruit-art {
    background: radial-gradient(ellipse 62% 50% at 52% 58%, var(--lime-art-b) 0%, var(--lime-art-a) 55%, rgba(233,239,106,0.25) 78%, rgba(255,255,255,0) 92%),
                radial-gradient(circle at 30% 20%, var(--lime-art-c) 0 13%, transparent 14%);
  }
  .can-face--strawberry .fruit-art {
    background: radial-gradient(ellipse 62% 50% at 52% 56%, var(--berry-art-b) 0%, var(--berry-art-a) 55%, rgba(240,88,78,0.25) 78%, rgba(255,255,255,0) 92%),
                radial-gradient(circle at 42% 18%, var(--berry-art-c) 0 12%, transparent 13%);
  }
  .brand-name {
    position: absolute; top: 180px; left: 0; right: 0;
    text-align: center;
    font-weight: 600; font-size: 118px; line-height: 1;
    color: var(--white);
  }

  .product-type {
    position: absolute; top: 502px - 0px; top: 362px; left: 0; right: 0;
    text-align: center; font-weight: 400; font-size: 16px;
  }
  .flavour-pill {
    position: absolute; top: 398px; left: 43px; width: 128px; height: 37px;
    border-radius: 18px;
    display: flex; align-items: center; justify-content: center;
    font-size: 15px; font-weight: 400;
  }
  .can-face--lemon-lime .flavour-pill { background: var(--lime-light); color: var(--lime-yellow); }
  .can-face--strawberry .flavour-pill { background: var(--berry); color: var(--white); }

  .feature-row {
    position: absolute; top: 446px; left: 8px; width: 202px; height: 72px;
  }
  .feature-row text { font-family: "Poppins", sans-serif; font-size: 6.2px; letter-spacing: 0.6px; fill: var(--accent); }
  .feature-row .icon { fill: none; stroke: var(--accent); stroke-width: 1.4; stroke-linecap: round; stroke-linejoin: round; }

  .can-volume {
    position: absolute; top: 530px; left: 0; right: 0;
    text-align: center; font-size: 10px; font-weight: 400;
  }
</style>
</head>
<body>

<section class="can-face can-face--lemon-lime" aria-label="Lemon and Lime can design">
  <div class="health-band">SUPPORTS GUT &amp; OVERALL HEALTH</div>
  <div class="fruit-art" role="img" aria-label="Lemon and lime fruit photography with green and yellow splash shapes"></div>
  <div class="kcal-badge"><span class="kcal-number">17</span><span class="kcal-unit">kcals</span></div>
  <div class="brand-name">zé</div>
  <div class="product-type">Prebiotic Fibre Drink</div>
  <div class="flavour-pill">Lemon &amp; Lime</div>
  <svg class="feature-row" viewBox="0 0 202 72" aria-label="20% of daily fibre, 0g sugar, nothing artificial">
    <defs>
      <path id="arc-l1" d="M14 36 A24 24 0 0 0 62 36"/>
      <path id="arc-l2" d="M78 38 A24 24 0 0 0 126 38"/>
      <path id="arc-l3" d="M142 36 A24 24 0 0 0 190 36"/>
    </defs>
    <path class="icon" d="M16 28 A24 24 0 0 1 60 26"/>
    <path class="icon" d="M38 48 L38 26 M38 32 q-6 -2 -6 -8 M38 32 q6 -2 6 -8 M38 40 q-6 -2 -6 -8 M38 40 q6 -2 6 -8"/>
    <text><textPath href="#arc-l1" startOffset="50%" text-anchor="middle">20% OF DAILY FIBRE</textPath></text>
    <circle class="icon" cx="102" cy="38" r="28"/>
    <path class="icon" d="M90 30 l8 -4 l8 4 l-8 4 z M90 30 v9 l8 4 v-9 M106 30 v9 l-8 4 M100 38 l8 -3 l8 3 v9 l-8 4 l-8 -4 z M82 58 L122 18"/>
    <text><textPath href="#arc-l2" startOffset="50%" text-anchor="middle">0G SUGAR</textPath></text>
    <path class="icon" d="M144 26 A24 24 0 0 1 188 28"/>
    <path class="icon" d="M160 20 l6 6 l-4 4 l-6 -6 z M164 28 l10 12 l-2 2 l-10 -12 M174 42 l2 6"/>
    <text><textPath href="#arc-l3" startOffset="50%" text-anchor="middle">NOTHING ARTIFICIAL</textPath></text>
  </svg>
  <div class="can-volume">8,5fl oz (250 ml)℮</div>
</section>

<section class="can-face can-face--strawberry" aria-label="Strawberry can design">
  <div class="health-band">SUPPORTS GUT &amp; OVERALL HEALTH</div>
  <div class="fruit-art" role="img" aria-label="Strawberry fruit photography with red splash shapes"></div>
  <div class="kcal-badge"><span class="kcal-number">17</span><span class="kcal-unit">kcals</span></div>
  <div class="brand-name">zé</div>
  <div class="product-type">Prebiotic Fibre Drink</div>
  <div class="flavour-pill">Strawberry</div>
  <svg class="feature-row" viewBox="0 0 202 72" aria-label="20% of daily fibre, 0g sugar, nothing artificial">
    <defs>
      <path id="arc-s1" d="M14 36 A24 24 0 0 0 62 36"/>
      <path id="arc-s2" d="M78 38 A24 24 0 0 0 126 38"/>
      <path id="arc-s3" d="M142 36 A24 24 0 0 0 190 36"/>
    </defs>
    <path class="icon" d="M16 28 A24 24 0 0 1 60 26"/>
    <path class="icon" d="M38 48 L38 26 M38 32 q-6 -2 -6 -8 M38 32 q6 -2 6 -8 M38 40 q-6 -2 -6 -8 M38 40 q6 -2 6 -8"/>
    <text><textPath href="#arc-s1" startOffset="50%" text-anchor="middle">20% OF DAILY FIBRE</textPath></text>
    <circle class="icon" cx="102" cy="38" r="28"/>
    <path class="icon" d="M90 30 l8 -4 l8 4 l-8 4 z M90 30 v9 l8 4 v-9 M106 30 v9 l-8 4 M100 38 l8 -3 l8 3 v9 l-8 4 l-8 -4 z M82 58 L122 18"/>
    <text><textPath href="#arc-s2" startOffset="50%" text-anchor="middle">0G SUGAR</textPath></text>
    <path class="icon" d="M144 26 A24 24 0 0 1 188 28"/>
    <path class="icon" d="M160 20 l6 6 l-4 4 l-6 -6 z M164 28 l10 12 l-2 2 l-10 -12 M174 42 l2 6"/>
    <text><textPath href="#arc-s3" startOffset="50%" text-anchor="middle">NOTHING ARTIFICIAL</textPath></text>
  </svg>
  <div class="can-volume">8,5fl oz (250 ml)℮</div>
</section>

</body>
</html>
```